Letterhead for TR Dealership
Harborline Vestra Orlan KTR
Project: Letterhead for TR Dealership
Letterhead for TR Dealership -
Creative Brief
Professional
Locations: Harborline Orlan KTR 4170 N. Tamsworth Avenue Richmond, VA 23287 Harborline Vestra KTR 1983 Pellway Hwy Powhatan, VA 23176 Commercial & Fleet Department 4170 N. Tamsworth Avenue Richmond, VA 23287
(804) 555-0172 Richmond (804) 555-0148 Powhatan
jmarvin@gohalvern.example
www.GoHalvern.example
Letterhead needs to reflect both locations and all brands. Vestra Orlan KTR check out our website: www.GoHalvern.example Red Fox is our company mascot. Can email logo design.

```html
<!DOCTYPE html>
<html lang="en">
<head>
<meta charset="utf-8">
<title>Harborline Vestra Orlan KTR – Stationery</title>
<link href="https://fonts.googleapis.com/css2?family=Roboto+Condensed:wght@400;700&family=Roboto:wght@400;500&display=swap" rel="stylesheet">
<style>
  :root{
    --bg:#e9eaec;
    --paper:#ffffff;
    --blue-deep:#0d1f6b;
    --blue:#1d4fd8;
    --blue-bright:#3f7cf2;
    --blue-pale:#e6eefc;
    --red:#d3202a;
    --ink:#1b1f2a;
    --ink-soft:#5a6272;
    --shadow:0 4px 14px rgba(0,0,0,.18);
  }
  *{box-sizing:border-box;margin:0;padding:0}
  html,body{width:1200px;height:713px;overflow:hidden}
  body{background:var(--bg);font-family:"Roboto",Arial,sans-serif;color:var(--ink);position:relative}

  .sheet{position:absolute;background:var(--paper);box-shadow:var(--shadow);overflow:hidden}

  /* logo lockup */
  .logo{display:flex;align-items:center;gap:6px;background:var(--paper);padding:5px 8px}
  .logo-mark{width:18px;height:18px;background:var(--ink);flex:none}
  .logo-name{font-family:"Roboto Condensed",Arial,sans-serif;font-weight:700;color:var(--blue-deep);font-size:19px;letter-spacing:.5px;line-height:1;text-transform:uppercase}
  .logo-brands{font-family:"Roboto Condensed",Arial,sans-serif;font-size:7px;color:var(--red);letter-spacing:1.5px;margin-top:2px}

  /* header band */
  .band{position:absolute;left:0;right:0;top:0;background:linear-gradient(90deg,var(--blue-deep),var(--blue) 60%,var(--blue-bright));border-bottom:3px solid var(--red);display:flex;align-items:center;justify-content:space-between;padding:0 12px}
  .band-contact{color:#fff;font-size:6.5px;line-height:1.5;text-align:left}

  .sheet-fade{position:absolute;left:0;right:0;background:linear-gradient(180deg,var(--blue-pale),var(--paper))}

  .mascot{position:absolute;border-radius:50%;background:radial-gradient(circle,#cfdcf6 0%,rgba(207,220,246,0) 70%)}

  .locations{position:absolute;font-size:6px;line-height:1.55;color:var(--ink-soft)}
  .locations strong{color:var(--blue);font-weight:500}
  .foot-rule{position:absolute;left:0;right:0;bottom:0;height:6px;background:linear-gradient(90deg,var(--blue-deep),var(--blue-bright))}

  /* letterhead */
  .letterhead{left:480px;top:28px;width:400px;height:518px}
  .letterhead .band{height:44px}
  .letterhead .sheet-fade{top:47px;height:160px}
  .letterhead .mascot{left:140px;top:190px;width:150px;height:150px}
  .letterhead .locations{left:26px;bottom:14px}

  /* envelope back */
  .envelope-back{left:40px;top:60px;width:400px;height:180px}
  .flap{position:absolute;left:0;top:0}
  .flap-seal{position:absolute;left:184px;top:40px;width:32px;height:32px;border-radius:50%;background:var(--blue-deep);opacity:.7}

  /* envelope front */
  .envelope-front{left:40px;top:280px;width:400px;height:180px}
  .envelope-front .band{height:38px}
  .envelope-front .sheet-fade{top:41px;height:70px}
  .envelope-front .locations{left:14px;bottom:14px}

  /* business card */
  .card{left:912px;top:60px;width:250px;height:145px}
  .card .band{height:34px;padding:0 8px}
  .card .band .logo{padding:4px 6px}
  .card .band .logo-name{font-size:14px}
  .card-person{position:absolute;right:12px;top:48px;text-align:right}
  .card-name{font-family:"Roboto Condensed",Arial,sans-serif;font-weight:700;font-size:12px;color:var(--blue-deep)}
  .card-title{font-size:7px;color:var(--red);letter-spacing:.5px;text-transform:uppercase}
  .card-contact{position:absolute;right:12px;top:82px;font-size:6.5px;line-height:1.5;text-align:right;color:var(--ink-soft)}
  .card .foot-rule{height:5px}

  /* standalone logo */
  .logo-tile{left:912px;top:240px;width:250px;height:80px;display:flex;align-items:center;justify-content:center}
  .logo-tile .logo-mark{width:34px;height:34px}
  .logo-tile .logo-name{font-size:32px}
  .logo-tile .logo-brands{font-size:9px}
</style>
</head>
<body>

  <!-- Letterhead -->
  <section class="sheet letterhead">
    <div class="sheet-fade"></div>
    <header class="band">
      <div class="logo">
        <span class="logo-mark"></span>
        <div><div class="logo-name">Harborline</div><div class="logo-brands">VESTRA • ORLAN • KTR</div></div>
      </div>
      <div class="band-contact">
        P: (804) 555-0172 Richmond<br>
        (804) 555-0148 Powhatan<br>
        E: jmarvin@gohalvern.example<br>
        www.GoHalvern.example
      </div>
    </header>
    <div class="mascot" role="img" aria-label="Faint Red Fox mascot watermark"></div>
    <div class="locations">
      <strong>Locations:</strong><br>
      Harborline Orlan KTR  4170 N. Tamsworth Avenue Richmond, VA 23287<br>
      Harborline Vestra KTR  1983 Pellway Hwy Powhatan, VA 23176<br>
      Commercial &amp; Fleet Department  4170 N. Tamsworth Avenue Richmond, VA 23287
    </div>
    <div class="foot-rule"></div>
  </section>

  <!-- Envelope back -->
  <section class="sheet envelope-back">
    <svg class="flap" width="400" height="110" viewBox="0 0 400 110" aria-hidden="true">
      <defs>
        <linearGradient id="flapFill" x1="0" y1="0" x2="0" y2="1">
          <stop offset="0" stop-color="#3f7cf2"/>
          <stop offset="1" stop-color="#0d1f6b"/>
        </linearGradient>
      </defs>
      <path d="M0 0 H400 V20 Q300 60 200 100 Q100 60 0 20 Z" fill="url(#flapFill)"/>
    </svg>
    <div class="flap-seal" role="img" aria-label="Red Fox mascot emblem"></div>
  </section>

  <!-- Envelope front -->
  <section class="sheet envelope-front">
    <div class="sheet-fade"></div>
    <header class="band">
      <div class="logo">
        <span class="logo-mark"></span>
        <div><div class="logo-name">Harborline</div><div class="logo-brands">VESTRA • ORLAN • KTR</div></div>
      </div>
      <div class="band-contact">
        (804) 555-0172 Richmond<br>
        (804) 555-0148 Powhatan<br>
        www.GoHalvern.example
      </div>
    </header>
    <div class="locations">
      <strong>Locations:</strong><br>
      Harborline Orlan KTR  4170 N. Tamsworth Avenue Richmond, VA 23287<br>
      Harborline Vestra KTR  1983 Pellway Hwy Powhatan, VA 23176<br>
      Commercial &amp; Fleet Department  4170 N. Tamsworth Avenue Richmond, VA 23287
    </div>
  </section>

  <!-- Business card -->
  <section class="sheet card">
    <header class="band">
      <div class="logo">
        <span class="logo-mark"></span>
        <div class="logo-name">Harborline</div>
      </div>
    </header>
    <div class="card-person">
      <div class="card-name">Jordan Marvin</div>
      <div class="card-title">Sales Manager</div>
    </div>
    <div class="card-contact">
      (804) 555-0172 Richmond<br>
      (804) 555-0148 Powhatan<br>
      jmarvin@gohalvern.example<br>
      www.GoHalvern.example
    </div>
    <div class="foot-rule"></div>
  </section>

  <!-- Logo -->
  <section class="sheet logo-tile">
    <div class="logo">
      <span class="logo-mark"></span>
      <div><div class="logo-name">Harborline</div><div class="logo-brands">Richmond &amp; Powhatan Virginia</div></div>
    </div>
  </section>

</body>
</html>
```